New Zealand Export company needs business cards

We need new business cards to match our new logo for a company based in New Zealand who deal specifically with the Pacific Islands. We source, consolidate and ship products out of New Zealand to the Pacific Islands. Will attach our old ones and also new logo.
Would like the Islands we deal with and the areas of work we have access to, to be included on the business cards.

Contact Information for Business Card

T +64 9 571 3048
F +64 9 571 6285
12-18 Kowhai Lane, Drury, 2113
PO Box 814, Drury, Auckland 2247, New Zealand
www.falconfreight.example.nz
E sales@falconfreight.example.nz

Font styles to use
Sans Serif

Colors
85abd2
33a6d7
ffffff

Requirements
Must have
• A company of PWM

```html
<!DOCTYPE html>
<html lang="en">
<head>
<meta charset="utf-8">
<title>Falcon Freight – Business Cards</title>
<link rel="stylesheet" href="https://fonts.googleapis.com/css2?family=Poppins:wght@400;500;600;700&display=swap">
<style>
  :root {
    --brand-blue: #1b5fae;
    --accent-blue: #33a6d7;
    --soft-blue: #85abd2;
    --white: #ffffff;
    --ink: #1c1c1c;
    --backdrop: #e7e9ec;
    --sky-top: #a9c9e8;
    --sky-bottom: #dfeaf3;
    --sea: #a7c9c4;
  }
  * { box-sizing: border-box; margin: 0; padding: 0; }
  html, body { width: 1200px; height: 900px; overflow: hidden; }
  body {
    background: var(--backdrop);
    font-family: "Poppins", sans-serif;
    display: flex;
    align-items: center;
    justify-content: center;
    gap: 40px;
  }
  .card {
    position: relative;
    width: 540px;
    height: 309px;
    border-radius: 20px;
    overflow: hidden;
    background: var(--white);
    box-shadow: 0 6px 18px rgba(0,0,0,.15);
  }

  /* Front */
  .front .band {
    position: absolute; left: 0; right: 0; bottom: 0; height: 92px;
    background: var(--brand-blue);
  }
  .front .person { position: absolute; left: 36px; top: 34px; }
  .front .name {
    color: var(--brand-blue); font-weight: 700; font-size: 22px; letter-spacing: 1.5px;
  }
  .front .role { color: var(--ink); font-size: 10px; font-weight: 500; margin-top: -2px; }
  .front .contacts { margin-top: 14px; font-size: 11.5px; color: var(--ink); line-height: 1.5; }
  .front .contacts .label { color: var(--accent-blue); font-weight: 600; margin-right: 6px; }
  .front .brand {
    position: absolute; right: 34px; top: 58px;
    display: flex; align-items: center; gap: 10px;
    color: var(--brand-blue); font-weight: 700; font-size: 24px; letter-spacing: 1px;
  }
  .front .brand .mark { width: 22px; height: 22px; background: var(--accent-blue); }
  .front .divider {
    position: absolute; left: 290px; top: 144px; width: 2px; height: 60px;
    background: var(--accent-blue);
  }
  .front .address {
    position: absolute; right: 34px; top: 140px; text-align: right;
    font-size: 13px; font-weight: 500; color: var(--ink); line-height: 1.55;
  }
  .front .web {
    position: absolute; left: 36px; bottom: 34px;
    color: var(--white); font-weight: 600; font-size: 13px; letter-spacing: 2.2px;
    text-transform: uppercase;
  }

  /* Back */
  .back .scene {
    position: absolute; left: 0; right: 0; top: 0; height: 220px;
    background: linear-gradient(180deg, var(--sky-top) 0%, var(--sky-bottom) 55%, var(--sea) 100%);
  }
  .back .sectors {
    position: absolute; left: 30px; right: 30px; top: 22px; text-align: center;
    color: var(--brand-blue); font-weight: 500; font-size: 12px; line-height: 1.45;
    text-transform: uppercase;
  }
  .back .band {
    position: absolute; left: 0; right: 0; bottom: 0; height: 89px;
    background: var(--brand-blue);
    display: flex; align-items: center; justify-content: center;
    padding: 0 24px; text-align: center;
    color: var(--white); font-weight: 500; font-size: 12.5px; line-height: 1.5;
    text-transform: uppercase;
  }
</style>
</head>
<body>
  <section class="card front">
    <div class="person">
      <p class="name">MARCUS HALE</p>
      <p class="role">DIRECTOR</p>
      <div class="contacts">
        <p><span class="label">T</span>+64 9 571 3048</p>
        <p><span class="label">F</span>+64 9 571 6285</p>
        <p>sales@falconfreight.example.nz</p>
      </div>
    </div>
    <div class="brand"><span class="mark"></span><span>FALCON FREIGHT</span></div>
    <div class="band"></div>
    <div class="divider"></div>
    <div class="address">
      <p>12-18 Kowhai Lane, Drury, 2113</p>
      <p>PO Box 814, Drury</p>
      <p>Auckland 2247, New Zealand</p>
    </div>
    <p class="web">www.falconfreight.example.nz</p>
  </section>

  <section class="card back">
    <div class="scene" role="img" aria-label="Photograph of a small tropical island with palm trees and calm lagoon water under a blue sky"></div>
    <p class="sectors">Hardware, Automative, Homewares, Aid Solutions, Hospitality, Safety<br>Equipment, Environmental Resources</p>
    <div class="band">
      <p>Cook Islands, Papua New Gunea, Tahiti, Tuvalu, Tokelau, Fiji, Kiribati<br>Samoa, New Caledonia, Tonga, Norfolk Islands</p>
    </div>
  </section>
</body>
</html>
```